Womans Supplement Designs

Launching a Supplement company and need to get some initial designs created, I've attached our logo and the bottle type that I want the samples done one.

This project is for our Whey Protein we are starting with Vanilla, chocolate and strawberry banana

(ALL DESIGN VARIATIONS MUST BE A WHITE BOTTLE NOT BLACK)

(FOR DESIGN SAMPLES PLEASE USE THE SUPPLEMENT BOTTLE STYLE I PROVIDED)

Whoever is selected the winner I will have more work for you to complete the disigns for the rest of the products in the line, Just want to get this shake completed first

Target Market(s)

Women

Requirements
Must have
• Must have our current logo involved

the name of this product will be "KIVA LUM"

Must have this slogan,

ALL-IN-ONE PREMIUM PROTEIN NUTRITIONAL SHAKE FOR BLACK WOMEN

This is our meal replacement

the design should try to keep the same look and feel of the existing provided supplement images

we are starting with chocolate, vanilla and strawberry banana

this is for women and should look colorful and appeal to them
Should not have
• Do not use an image of a person or lady, don't want it branded to a person

```html
<!DOCTYPE html>
<html lang="en">
<head>
<meta charset="utf-8">
<title>KIVA LUM – Protein Shake Labels</title>
<link rel="stylesheet" href="https://fonts.googleapis.com/css2?family=Bebas+Neue&family=Oswald:wght@500;600&family=Kaushan+Script&family=Montserrat:wght@500;700&display=swap">
<style>
  :root {
    --page: #ffffff;
    --ink: #1d1d1d;
    --title: #2a2a2a;
    --panel-line: #cfcfcf;
    --muted: #555555;
    --band-dark: #1a1a1a;
  }
  * { box-sizing: border-box; margin: 0; padding: 0; }
  html, body { width: 1200px; height: 1200px; overflow: hidden; background: var(--page); }
  .canvas {
    position: relative; width: 1200px; height: 1200px;
    display: flex; gap: 20px; justify-content: center; align-items: center;
  }
  .label {
    position: relative; width: 380px; height: 520px; background: #fff;
    overflow: hidden; box-shadow: 0 0 0 1px #ececec;
    font-family: "Montserrat", sans-serif; color: var(--ink);
  }
  .label--chocolate {
    --stripe-a: #8a3a1a; --stripe-b: #d8b29c;
    --flavor-bg: #8b4a2b; --flavor-text: #ffffff;
    --supp-bg: #b3732b; --supp-text: #ffffff;
    --tags-bg: #7a2e12; --tags-text: #e3a254;
  }
  .label--vanilla {
    --stripe-a: #e3cf8c; --stripe-b: #f3e8c2;
    --flavor-bg: #e2d19a; --flavor-text: #ffffff;
    --supp-bg: #cdcdcd; --supp-text: #6a6a6a;
    --tags-bg: #efe3b4; --tags-text: #777777;
  }
  .label--strawberry {
    --stripe-a: #d81f35; --stripe-b: #f28090;
    --flavor-bg: #d81f35; --flavor-text: #ffffff;
    --supp-bg: #e6b529; --supp-text: #ffffff;
    --tags-bg: #d81f35; --tags-text: #f3c93a;
  }
  .top-stripe {
    position: absolute; left: 0; right: 0; top: 22px; height: 16px;
    background: linear-gradient(90deg, var(--stripe-a), var(--stripe-b) 50%, var(--stripe-a));
  }
  .brand-badge { position: absolute; left: 95px; top: 0; width: 190px; height: 150px; }
  .brand-name {
    position: absolute; left: 0; right: 0; top: 58px; text-align: center;
    color: #fff; font-size: 11px; font-weight: 500; letter-spacing: 2px;
  }
  .brand-dot {
    position: absolute; left: 50%; top: 28px; width: 18px; height: 18px;
    margin-left: -9px; border-radius: 50%; background: #fff;
  }
  .product-name {
    position: absolute; left: 84px; right: 84px; top: 152px; text-align: center;
    font-family: "Bebas Neue", sans-serif; font-size: 62px; font-weight: 400; line-height: 1;
    color: var(--title); letter-spacing: 0; white-space: nowrap;
  }
  .slogan {
    position: absolute; left: 84px; right: 84px; top: 228px; text-align: center;
    font-family: "Oswald", sans-serif; font-weight: 600; font-size: 15px;
    line-height: 1.2; color: var(--ink); letter-spacing: -0.3px; text-transform: uppercase;
    white-space: nowrap;
  }
  .info-panel, .facts-panel {
    position: absolute; top: 118px; width: 68px; height: 192px; overflow: hidden;
    border: 1px solid var(--panel-line); padding: 5px 4px;
    font-size: 5.5px; line-height: 1.35; color: var(--muted);
  }
  .info-panel { left: 10px; }
  .facts-panel { right: 10px; }
  .panel-title {
    font-family: "Oswald", sans-serif; font-size: 7.5px; font-weight: 600;
    color: var(--ink); margin-bottom: 4px; line-height: 1.2;
  }
  .info-panel p { margin-bottom: 4px; }
  .marks { display: flex; gap: 3px; margin-top: 8px; }
  .marks span { width: 11px; height: 11px; border-radius: 50%; border: 1px solid #999; }
  .facts-head { background: #333; color: #fff; padding: 2px; margin-bottom: 3px; }
  .facts-row { display: flex; justify-content: space-between; border-bottom: 0.5px solid #bbb; }
  .socials { display: flex; gap: 3px; margin-top: 10px; }
  .socials span { width: 9px; height: 9px; background: #444; }
  .flavor {
    position: absolute; left: 0; right: 0; top: 340px; height: 50px;
  }
  .flavor svg { position: absolute; inset: 0; }
  .flavor-name {
    position: absolute; left: 0; right: 0; top: 2px; text-align: center;
    font-family: "Kaushan Script", cursive; font-size: 32px; color: var(--flavor-text);
    white-space: nowrap;
  }
  .label--strawberry .flavor-name { font-size: 27px; top: 6px; }
  .supp-band {
    position: absolute; left: 0; right: 0; top: 390px; height: 32px;
    background: var(--supp-bg); color: var(--supp-text); text-align: center;
    font-size: 19px; font-weight: 700; letter-spacing: 1px; line-height: 32px;
  }
  .tags-band {
    position: absolute; left: 0; right: 0; top: 422px; height: 40px;
    background: var(--tags-bg); display: flex; justify-content: center; align-items: center;
    gap: 12px; color: var(--tags-text); font-size: 11px; font-weight: 500;
    text-align: center; line-height: 1.15;
  }
  .tags-band .sep { width: 5px; height: 5px; border-radius: 50%; background: #fff; }
  .net-band {
    position: absolute; left: 0; right: 0; top: 462px; bottom: 0;
    background: var(--band-dark); color: #fff; text-align: center;
    font-size: 19px; font-weight: 700; letter-spacing: 0.5px; line-height: 58px;
  }
</style>
</head>
<body>
<main class="canvas">

  <section class="label label--chocolate">
    <div class="top-stripe"></div>
    <svg class="brand-badge" viewBox="0 0 190 150"><polygon points="0,0 190,0 95,150" fill="#1a1a1a"/></svg>
    <div class="brand-badge"><span class="brand-dot"></span><div class="brand-name">SABLE GRACE</div></div>
    <aside class="info-panel">
      <div class="panel-title">DIETARY SUPPLEMENT</div>
      <p>Ingredients: whey protein blend, natural flavour, sunflower lecithin.</p>
      <p>Storage: keep in a cool dry place.</p>
      <p>Use: mix one scoop with water or milk after training.</p>
      <div class="marks"><span></span><span></span><span></span><span></span></div>
    </aside>
    <aside class="facts-panel">
      <div class="panel-title">Nutrition Facts</div>
      <div class="facts-head">Serving size 1 scoop</div>
      <div class="facts-row"><span>Calories</span><span>130</span></div>
      <div class="facts-row"><span>Total Fat</span><span>1g</span></div>
      <div class="facts-row"><span>Sodium</span><span>60mg</span></div>
      <div class="facts-row"><span>Carbs</span><span>3g</span></div>
      <div class="facts-row"><span>Protein</span><span>24g</span></div>
      <div class="facts-row"><span>Calcium</span><span>9%</span></div>
      <div class="socials"><span></span><span></span><span></span><span></span></div>
    </aside>
    <h1 class="product-name">KIVA LUM</h1>
    <p class="slogan">All-in-one premium protein<br>nutritional shake<br>for black women</p>
    <div class="flavor">
      <svg viewBox="0 0 380 50" preserveAspectRatio="none"><polygon points="120,0 260,0 290,50 90,50" fill="var(--flavor-bg)"/></svg>
      <div class="flavor-name">Chocolate</div>
    </div>
    <div class="supp-band">DIETARY SUPPLEMENT</div>
    <div class="tags-band"><span>GLUTEN<br>FREE</span><i class="sep"></i><span>SOY<br>FREE</span><i class="sep"></i><span>DAIRY<br>FREE</span><i class="sep"></i><span>VEGAN</span></div>
    <div class="net-band">NET WT. 5 LBS (2.26 KG)</div>
  </section>

  <section class="label label--vanilla">
    <div class="top-stripe"></div>
    <svg class="brand-badge" viewBox="0 0 190 150"><polygon points="0,0 190,0 95,150" fill="#1a1a1a"/></svg>
    <div class="brand-badge"><span class="brand-dot"></span><div class="brand-name">SABLE GRACE</div></div>
    <aside class="info-panel">
      <div class="panel-title">DIETARY SUPPLEMENT</div>
      <p>Ingredients: whey protein blend, natural flavour, sunflower lecithin.</p>
      <p>Storage: keep in a cool dry place.</p>
      <p>Use: mix one scoop with water or milk after training.</p>
      <div class="marks"><span></span><span></span><span></span><span></span></div>
    </aside>
    <aside class="facts-panel">
      <div class="panel-title">Nutrition Facts</div>
      <div class="facts-head">Serving size 1 scoop</div>
      <div class="facts-row"><span>Calories</span><span>130</span></div>
      <div class="facts-row"><span>Total Fat</span><span>1g</span></div>
      <div class="facts-row"><span>Sodium</span><span>60mg</span></div>
      <div class="facts-row"><span>Carbs</span><span>3g</span></div>
      <div class="facts-row"><span>Protein</span><span>24g</span></div>
      <div class="facts-row"><span>Calcium</span><span>9%</span></div>
      <div class="socials"><span></span><span></span><span></span><span></span></div>
    </aside>
    <h1 class="product-name">KIVA LUM</h1>
    <p class="slogan">All-in-one premium protein<br>nutritional shake<br>for black women</p>
    <div class="flavor">
      <svg viewBox="0 0 380 50" preserveAspectRatio="none"><polygon points="120,0 260,0 290,50 90,50" fill="var(--flavor-bg)"/></svg>
      <div class="flavor-name">Vanilla</div>
    </div>
    <div class="supp-band">DIETARY SUPPLEMENT</div>
    <div class="tags-band"><span>GLUTEN<br>FREE</span><i class="sep"></i><span>SOY<br>FREE</span><i class="sep"></i><span>DAIRY<br>FREE</span><i class="sep"></i><span>VEGAN</span></div>
    <div class="net-band">NET WT. 5 LBS (2.26 KG)</div>
  </section>

  <section class="label label--strawberry">
    <div class="top-stripe"></div>
    <svg class="brand-badge" viewBox="0 0 190 150"><polygon points="0,0 190,0 95,150" fill="#1a1a1a"/></svg>
    <div class="brand-badge"><span class="brand-dot"></span><div class="brand-name">SABLE GRACE</div></div>
    <aside class="info-panel">
      <div class="panel-title">DIETARY SUPPLEMENT</div>
      <p>Ingredients: whey protein blend, natural flavour, sunflower lecithin.</p>
      <p>Storage: keep in a cool dry place.</p>
      <p>Use: mix one scoop with water or milk after training.</p>
      <div class="marks"><span></span><span></span><span></span><span></span></div>
    </aside>
    <aside class="facts-panel">
      <div class="panel-title">Nutrition Facts</div>
      <div class="facts-head">Serving size 1 scoop</div>
      <div class="facts-row"><span>Calories</span><span>130</span></div>
      <div class="facts-row"><span>Total Fat</span><span>1g</span></div>
      <div class="facts-row"><span>Sodium</span><span>60mg</span></div>
      <div class="facts-row"><span>Carbs</span><span>3g</span></div>
      <div class="facts-row"><span>Protein</span><span>24g</span></div>
      <div class="facts-row"><span>Calcium</span><span>9%</span></div>
      <div class="socials"><span></span><span></span><span></span><span></span></div>
    </aside>
    <h1 class="product-name">KIVA LUM</h1>
    <p class="slogan">All-in-one premium protein<br>nutritional shake<br>for black women</p>
    <div class="flavor">
      <svg viewBox="0 0 380 50" preserveAspectRatio="none"><polygon points="70,0 320,0 345,50 45,50" fill="var(--flavor-bg)"/></svg>
      <div class="flavor-name">Strawberry Banana</div>
    </div>
    <div class="supp-band">DIETARY SUPPLEMENT</div>
    <div class="tags-band"><span>GLUTEN<br>FREE</span><i class="sep"></i><span>SOY<br>FREE</span><i class="sep"></i><span>DAIRY<br>FREE</span><i class="sep"></i><span>VEGAN</span></div>
    <div class="net-band">NET WT. 5 LBS (2.26 KG)</div>
  </section>

</main>
</body>
</html>
```